Flyerdesign for a Sports Homepage

I need a design for our Merchandise/Discount Flyer.
we are going to sell high class sports equipment.
the flyer should be in Size A5 or between A5 and A4.
there should be mentioned our Product names:
Product name for powerlifting: Torvik
Product name for Boxing: ZL Boxing
Product name for Martial Arts: Murelt
Product name for MMA: PitVolt
Product name for Bodybuilding: Bramfold

our Storename: PushAndDuel
Homepage: www.pushandduel.example

there should be space for entering a discount code
shop logo and brand logos: all pictures are attached.

out of the box thinking is welcome

Target Market(s)

People who do powersports like powerlifting or mma

Industry/Entity Type

Sport

Requirements
Must have
• 2 sides, all our brandnames, homepage, shop name and sports

```html
<!DOCTYPE html>
<html lang="en">
<head>
<meta charset="utf-8">
<title>PushAndDuel Flyer – Two Sides</title>
<link rel="stylesheet" href="https://fonts.googleapis.com/css2?family=Oswald:wght@400;500;600&family=Roboto+Condensed:wght@400;700&display=swap">
<style>
  :root {
    --page-bg: #dcdcdc;
    --card-bg: #121212;
    --card-bg-2: #222222;
    --header-black: #050505;
    --gold: #c9a95c;
    --gold-light: #e9d39a;
    --gold-dark: #8a6d2c;
    --white: #ffffff;
    --muted: #9a9a9a;
    --fire-hot: #ffd36a;
    --fire-1: #f39a1c;
    --fire-2: #d2400f;
    --fire-3: #7a1408;
    --fire-4: #2a0604;
    --violet: #3a0c30;
  }
  * { box-sizing: border-box; margin: 0; padding: 0; }
  html, body { width: 867px; height: 1200px; overflow: hidden; }
  body { background: var(--page-bg); font-family: "Roboto Condensed", Arial, sans-serif; position: relative; }

  .flyer {
    position: absolute; left: 79px; width: 726px; height: 512px;
    background: radial-gradient(ellipse at 70% 55%, var(--card-bg-2), var(--card-bg) 70%);
    overflow: hidden;
    box-shadow: 0 4px 12px rgba(0,0,0,.35);
  }
  .flyer--front { top: 70px; }
  .flyer--back { top: 624px; }

  .frame { position: absolute; inset: 0; width: 100%; height: 100%; }

  .photo { position: absolute; }
  .flyer--front .photo {
    left: 0; top: 80px; width: 380px; height: 382px;
    background:
      radial-gradient(ellipse 22% 18% at 48% 52%, rgba(255,211,106,.85), transparent 70%),
      radial-gradient(ellipse 30% 22% at 28% 80%, rgba(243,154,28,.8), transparent 75%),
      radial-gradient(ellipse 26% 20% at 70% 20%, rgba(210,64,15,.75), transparent 75%),
      radial-gradient(ellipse 40% 30% at 20% 25%, rgba(122,20,8,.9), transparent 80%),
      radial-gradient(ellipse 70% 60% at 45% 55%, var(--fire-2), var(--fire-3) 55%, var(--fire-4) 85%);
    -webkit-mask-image: linear-gradient(90deg, #000 65%, transparent 100%);
            mask-image: linear-gradient(90deg, #000 65%, transparent 100%);
  }
  .flyer--back .photo {
    left: 300px; top: 44px; width: 426px; height: 418px;
    background:
      radial-gradient(ellipse 18% 15% at 55% 30%, rgba(255,211,106,.85), transparent 70%),
      radial-gradient(ellipse 28% 20% at 75% 55%, rgba(243,154,28,.75), transparent 75%),
      radial-gradient(ellipse 25% 18% at 38% 62%, rgba(210,64,15,.8), transparent 75%),
      radial-gradient(ellipse 30% 20% at 60% 88%, rgba(122,20,8,.9), transparent 80%),
      radial-gradient(ellipse 70% 65% at 58% 45%, var(--fire-2), var(--fire-3) 50%, var(--violet) 85%);
    -webkit-mask-image: linear-gradient(90deg, transparent 0%, #000 30%);
            mask-image: linear-gradient(90deg, transparent 0%, #000 30%);
  }

  .brand {
    position: absolute; left: 21px; top: 20px; width: 101px; height: 63px;
    border: 1px solid var(--gold-dark);
    background: linear-gradient(180deg, #2a2a2a, #0c0c0c);
    display: flex; flex-direction: column; align-items: center; justify-content: center; gap: 6px;
  }
  .brand__mark { width: 22px; height: 22px; background: var(--gold); }
  .brand__name { font-family: "Oswald", sans-serif; font-size: 9px; color: var(--white); letter-spacing: .5px; }

  .tagline {
    position: absolute; left: 138px; top: 18px;
    font-family: "Oswald", sans-serif; font-weight: 500; font-size: 16px; line-height: 25px;
    color: var(--gold-light); text-transform: uppercase;
  }

  .social { position: absolute; right: 24px; top: 14px; display: flex; gap: 9px; }
  .social span { width: 16px; height: 16px; border: 1px solid var(--white); border-radius: 50%; }

  .badge {
    position: absolute; border-radius: 50%;
    border: 6px solid var(--gold-light);
    box-shadow: 0 0 0 2px var(--gold-dark), inset 0 0 0 2px #6b5320, inset 0 0 18px rgba(0,0,0,.8), 0 5px 12px rgba(0,0,0,.75);
    background:
      radial-gradient(ellipse 30% 22% at 50% 30%, rgba(243,154,28,.7), transparent 75%),
      radial-gradient(ellipse 35% 28% at 50% 62%, rgba(255,211,106,.8), transparent 70%),
      radial-gradient(circle at 50% 55%, var(--fire-2), var(--fire-3) 50%, #160403 85%);
  }

  .headline {
    position: absolute; right: 26px; top: 100px;
    font-family: "Oswald", sans-serif; font-weight: 500; font-size: 34px; color: var(--gold-light);
  }
  .product-list { position: absolute; right: 26px; top: 161px; list-style: none; text-align: right; }
  .product-list li {
    font-family: "Oswald", sans-serif; font-size: 14px; line-height: 36.6px; color: var(--white);
  }
  .product-list b { color: var(--gold-light); font-weight: 500; font-size: 16px; }

  .discount {
    position: absolute; right: 26px; top: 362px;
    font-family: "Oswald", sans-serif; font-weight: 600; font-size: 44px; color: var(--white); line-height: 56px;
  }
  .discount__amount { color: var(--gold); }
  .discount-code {
    position: absolute; right: 26px; top: 416px;
    font-family: "Oswald", sans-serif; font-size: 13px; color: var(--muted); letter-spacing: .5px;
  }
  .discount-code b { color: var(--white); font-weight: 500; font-size: 15px; }

  .section-title {
    position: absolute; left: 21px; top: 130px;
    font-family: "Oswald", sans-serif; font-weight: 500; font-size: 28px; color: var(--gold-light);
  }
  .intro { position: absolute; left: 21px; top: 182px; width: 330px; color: var(--white); font-size: 13px; line-height: 15px; }
  .intro p + p { margin-top: 10px; }

  .collection-label {
    position: absolute; width: 120px; text-align: center; top: 404px;
    font-family: "Oswald", sans-serif; color: var(--white);
  }
  .collection-label strong { display: block; color: var(--gold-light); font-weight: 500; font-size: 15px; line-height: 17px; }
  .collection-label span { font-size: 10px; text-transform: uppercase; }

  .footer-text {
    position: absolute; top: 478px; left: 20px; display: flex; gap: 14px; align-items: center;
    font-family: "Oswald", sans-serif; font-size: 12.5px; color: var(--white);
  }
  .footer-text svg { vertical-align: -2px; margin-right: 6px; }
  .website {
    position: absolute; top: 476px; right: 22px;
    font-family: "Oswald", sans-serif; font-weight: 500; font-size: 15px; color: #111; letter-spacing: 1px;
    display: flex; align-items: center; gap: 8px;
  }
</style>
</head>
<body>

<!-- Front side -->
<section class="flyer flyer--front">
  <div class="photo" role="img" aria-label="Collage of boxers and fighters in a ring surrounded by flames"></div>

  <svg class="frame" viewBox="0 0 726 512" aria-hidden="true">
    <defs>
      <linearGradient id="goldFront" x1="0" y1="0" x2="1" y2="1">
        <stop offset="0" stop-color="#f1dea6"/><stop offset=".5" stop-color="#c9a95c"/><stop offset="1" stop-color="#7d6127"/>
      </linearGradient>
    </defs>
    <polygon points="400,44 440,44 230,462 190,462" fill="url(#goldFront)" opacity=".8"/>
    <polygon points="452,44 458,44 248,462 242,462" fill="#c9a95c" opacity=".45"/>
    <polygon points="0,0 726,0 726,43 400,43 360,101 0,101" fill="#050505"/>
    <polyline points="0,102 361,102 401,44 726,44" fill="none" stroke="url(#goldFront)" stroke-width="2.5"/>
    <rect x="0" y="462" width="726" height="50" fill="#050505"/>
    <line x1="0" y1="459" x2="726" y2="459" stroke="url(#goldFront)" stroke-width="2.5"/>
    <polygon points="480,466 726,466 726,512 456,512" fill="url(#goldFront)"/>
  </svg>

  <div class="brand"><span class="brand__mark"></span><span class="brand__name">PUSH AND DUEL</span></div>
  <p class="tagline">Premium quality<br>products for all lifting<br>and fighting sports</p>
  <div class="social" aria-label="Social links"><span></span><span></span><span></span></div>

  <div class="badge" style="left:356px;top:73px;width:112px;height:112px" role="img" aria-label="PitVolt brand artwork"></div>
  <div class="badge" style="left:308px;top:197px;width:112px;height:112px" role="img" aria-label="Torvik brand artwork"></div>
  <div class="badge" style="left:234px;top:321px;width:112px;height:112px" role="img" aria-label="Murelt brand artwork"></div>

  <h1 class="headline">PUSH AND DUEL</h1>
  <ul class="product-list">
    <li>Product name for powerlifting: <b>TORVIK</b></li>
    <li>Product name for Boxing: <b>ZL BOXING</b></li>
    <li>Product name for Martial Arts: <b>MURELT</b></li>
    <li>Product name for MMA: <b>PITVOLT</b></li>
    <li>Product name for Bodybuilding: <b>BRAMFOLD</b></li>
  </ul>
  <p class="discount"><span class="discount__amount">€50,00</span> DISCOUNT</p>
  <p class="discount-code">ENTERING A DISCOUNT CODE: <b>0000 000</b></p>

  <p class="footer-text">
    <span><svg width="9" height="12" viewBox="0 0 9 12"><path d="M4.5 0A4.5 4.5 0 0 0 0 4.5C0 8 4.5 12 4.5 12S9 8 9 4.5A4.5 4.5 0 0 0 4.5 0zm0 6.3a1.8 1.8 0 1 1 0-3.6 1.8 1.8 0 0 1 0 3.6z" fill="#c9a95c"/></svg>KARVENHOLT UG Lindenweg 4, 04109 Musterstadt</span>
    <span><svg width="13" height="9" viewBox="0 0 13 9"><rect width="13" height="9" fill="#c9a95c"/><polyline points="0,0 6.5,5 13,0" fill="none" stroke="#050505" stroke-width="1.2"/></svg>info@karvenholt.example</span>
  </p>
  <p class="website"><svg width="14" height="14" viewBox="0 0 14 14"><circle cx="7" cy="7" r="6" fill="none" stroke="#111" stroke-width="1.6"/><circle cx="7" cy="7" r="2" fill="#111"/></svg>WWW.PUSHANDDUEL.EXAMPLE</p>
</section>

<!-- Back side -->
<section class="flyer flyer--back">
  <div class="photo" role="img" aria-label="Martial artists and fighters in action with flames and a ring in the background"></div>

  <svg class="frame" viewBox="0 0 726 512" aria-hidden="true">
    <defs>
      <linearGradient id="goldBack" x1="0" y1="0" x2="1" y2="1">
        <stop offset="0" stop-color="#f1dea6"/><stop offset=".5" stop-color="#c9a95c"/><stop offset="1" stop-color="#7d6127"/>
      </linearGradient>
    </defs>
    <polygon points="400,44 436,44 270,462 234,462" fill="url(#goldBack)" opacity=".7"/>
    <polygon points="0,0 726,0 726,43 400,43 360,101 0,101" fill="#050505"/>
    <polyline points="0,102 361,102 401,44 726,44" fill="none" stroke="url(#goldBack)" stroke-width="2.5"/>
    <rect x="0" y="462" width="726" height="50" fill="#050505"/>
    <line x1="0" y1="459" x2="726" y2="459" stroke="url(#goldBack)" stroke-width="2.5"/>
    <polygon points="480,466 726,466 726,512 456,512" fill="url(#goldBack)"/>
  </svg>

  <div class="brand"><span class="brand__mark"></span><span class="brand__name">PUSH AND DUEL</span></div>
  <p class="tagline">Premium quality<br>products for all lifting<br>and fighting sports</p>
  <div class="social" aria-label="Social links"><span></span><span></span><span></span></div>

  <h2 class="section-title">OUR COLLECTIONS</h2>
  <div class="intro">
    <p>PushAndDuel is dedicated to get you Premium Quality Products for all Lifting and Fighting Sports.</p>
    <p>We focus on Customer Support and getting you products which assists you on reaching new personal records</p>
  </div>

  <div class="badge" style="left:46px;top:280px;width:106px;height:106px" role="img" aria-label="Torvik powerlifting artwork"></div>
  <div class="badge" style="left:176px;top:280px;width:106px;height:106px" role="img" aria-label="ZL Boxing artwork"></div>
  <div class="badge" style="left:308px;top:280px;width:106px;height:106px" role="img" aria-label="Murelt martial arts artwork"></div>
  <div class="badge" style="left:441px;top:280px;width:106px;height:106px" role="img" aria-label="PitVolt MMA artwork"></div>
  <div class="badge" style="left:574px;top:280px;width:106px;height:106px" role="img" aria-label="Bramfold bodybuilding artwork"></div>

  <p class="collection-label" style="left:39px"><strong>TORVIK</strong><span>Powerlifting</span></p>
  <p class="collection-label" style="left:169px"><strong>ZL BOXING</strong><span>Boxing</span></p>
  <p class="collection-label" style="left:301px"><strong>MURELT</strong><span>Martial Arts</span></p>
  <p class="collection-label" style="left:434px"><strong>PITVOLT</strong><span>MMA</span></p>
  <p class="collection-label" style="left:567px"><strong>BRAMFOLD</strong><span>Bodybuilding</span></p>

  <p class="footer-text">
    <span><svg width="9" height="12" viewBox="0 0 9 12"><path d="M4.5 0A4.5 4.5 0 0 0 0 4.5C0 8 4.5 12 4.5 12S9 8 9 4.5A4.5 4.5 0 0 0 4.5 0zm0 6.3a1.8 1.8 0 1 1 0-3.6 1.8 1.8 0 0 1 0 3.6z" fill="#c9a95c"/></svg>KARVENHOLT UG Lindenweg 4, 04109 Musterstadt</span>
    <span><svg width="13" height="9" viewBox="0 0 13 9"><rect width="13" height="9" fill="#c9a95c"/><polyline points="0,0 6.5,5 13,0" fill="none" stroke="#050505" stroke-width="1.2"/></svg>info@karvenholt.example</span>
  </p>
  <p class="website"><svg width="14" height="14" viewBox="0 0 14 14"><circle cx="7" cy="7" r="6" fill="none" stroke="#111" stroke-width="1.6"/><circle cx="7" cy="7" r="2" fill="#111"/></svg>WWW.PUSHANDDUEL.EXAMPLE</p>
</section>

</body>
</html>
```